Specialist Medical practice after professional trifold flyer design for patient information brochure

I am the Director of the Hollowbrook Clinic, a specialist medial and surgical practice in Australia. I am after a professional design of a patient information trifold flyer that can be used for web distribution or for commercial printing for upcoming educational event. The design would need to allow change of images and text to be used as template for future topics but have a common brand look across them. Colours would follow the logo, but primarily blue colours for the hollowbrook theme. The inside text needs to be clearly contrasted to the background for easy reading, as often elderly patients. The design would make use of curves or circles, but open for hexagonal, triangle square vector components. I have included an outline for the initial brochure and included images to include. Other stock background images can be used if they increase the impact of the design over included. A winning design is also one that could be modified to a 4 page bi-fold brochure

Target Market(s)

This will be provided to patients in GP practices, podiatry clinics, radiological practices. Aimed at patients to read and be compelled to look to site or get consultation with me

Industry/Entity Type

Medical

Font styles to use
Serif
Sans Serif

Colors
33a6d7
0355a3
86cfc6
cedeed
0292cd
85cae6

Requirements
Must have
• The front cover needs to engage the patient to pick up and read- yes I have a painful ankle and want to find out more. the goal for the inside is to provide the options but be able to direct to website for more info - website currently undergoing upgrade. After professional modern look. Not bright contrasting colours like many advertising brochures. Needs to able to have images and text changed but following same look to create new topics
Nice to have
• The focus is a Tri-fold brochure. Nice to be able to modify to bifold. A winning design would even offer both, or submit separate bifold and trifold. I am open to different versions of similar look. (eg option of brochure with curved elements, triangular or square, or hexagonal.
Should not have
• To many contrasting colours. Text must be easily read on background, either white or coloured background texture with transparency

```html
<!DOCTYPE html>
<html lang="en">
<head>
<meta charset="utf-8">
<title>My Painful Ankle – Trifold Brochure</title>
<link href="https://fonts.googleapis.com/css2?family=Roboto:wght@300;400;500;700&family=Oswald:wght@300;400&display=swap" rel="stylesheet">
<style>
:root{
  --backdrop:#8e8e8e;
  --blue-deep:#0355a3;
  --blue:#0292cd;
  --blue-mid:#33a6d7;
  --blue-soft:#85cae6;
  --teal:#86cfc6;
  --teal-strong:#3fb8a8;
  --mist:#cedeed;
  --ink:#3a3a3a;
  --white:#ffffff;
  --panel-tint:#f6f7f9;
}
*{box-sizing:border-box;margin:0;padding:0}
html,body{width:802px;height:1200px;overflow:hidden}
body{background:var(--backdrop);font-family:"Roboto",sans-serif;color:var(--ink);position:relative}
.side-label{position:absolute;left:0;width:802px;text-align:center;color:var(--white);font-family:"Roboto",sans-serif;font-weight:400;font-size:34px;letter-spacing:1px}
.side-label--front{top:48px}
.side-label--back{top:1130px}
.sheet{position:absolute;left:84px;width:634px;height:492px;background:var(--white);overflow:hidden;box-shadow:0 12px 14px -8px rgba(0,0,0,.45)}
.sheet--front{top:96px}
.sheet--back{top:622px}
.abs{position:absolute}
.decor{position:absolute;left:0;top:0;width:634px;height:492px}
.panel-tint{position:absolute;top:0;height:492px;background:var(--panel-tint)}

/* front left */
.portrait{left:0;top:0;width:207px;height:190px;background:linear-gradient(180deg,#eef0f2 0%,#d9dde2 60%,#c7ccd3 100%)}
.bio{left:10px;width:187px;color:var(--white);text-align:center}
.bio__name{top:208px;font-family:"Roboto",sans-serif;font-weight:500;font-size:14.5px;letter-spacing:.2px}
.bio__creds{top:228px;font-size:6px}
.bio__text{top:243px;font-size:6.6px;line-height:9.6px;font-weight:300;text-align:justify;text-align-last:center}
.conditions__title{top:317px;left:10px;width:187px;text-align:center;color:var(--white);font-weight:400;font-size:13px}
.conditions__intro{top:339px;left:10px;width:187px;text-align:center;color:var(--white);font-size:6px;line-height:9px;font-weight:300}
.conditions__list{top:0;left:10px;width:188px;height:492px;list-style:none;color:var(--white);font-size:5.8px;line-height:9px;font-weight:300}
.conditions__list li{position:absolute;left:0;width:188px;padding:0 0 2px 9px;border-bottom:.6px solid rgba(255,255,255,.55)}
.conditions__list svg{position:absolute;left:0;top:1px;width:6.5px;height:6.5px}

/* front middle */
.hero-photo{left:207px;top:0;width:427px;height:360px;background:linear-gradient(160deg,#c7c1a8 0%,#f4e3a8 30%,#e8c27a 52%,#b7a466 72%,#8a8a55 100%)}
.building-photo{left:230px;top:136px;width:168px;height:168px;border-radius:50%;border:5px solid var(--white);background:linear-gradient(160deg,#9fc3e4 0%,#dfe8f0 45%,#8b9198 75%,#4f5e3a 100%);box-shadow:0 2px 6px rgba(0,0,0,.25)}
.contact{left:207px;width:210px;text-align:center}
.contact__title{top:314px;font-family:"Oswald",sans-serif;font-weight:300;font-size:19px;color:#4a4a4a;letter-spacing:.3px}
.contact__list{top:342px;list-style:none;font-size:7.8px;line-height:13.6px;color:#555}
.contact__list svg{width:7px;height:7px;vertical-align:-1px;margin-right:3px}
.brand{display:flex;align-items:center;justify-content:center;gap:5px;width:210px}
.brand__dot{width:20px;height:20px;border-radius:50%;border:2.5px solid var(--blue-deep)}
.brand__name{font-family:"Roboto",sans-serif;font-weight:700;font-size:10.5px;color:var(--blue-deep);letter-spacing:.2px;text-transform:uppercase}
.brand--contact{left:207px;top:457px}
.brand--cover{left:417px;top:455px;width:217px}

/* front right */
.cover__title{left:417px;top:366px;width:217px;text-align:center;color:var(--blue-deep);font-weight:700;font-size:18px;letter-spacing:.3px}
.cover__sub{left:417px;top:389px;width:217px;text-align:center;color:var(--teal-strong);font-weight:500;font-size:7.6px}
.cover__badge{left:437px;top:409px;width:176px;height:34px;border-radius:12px;background:var(--teal-strong);color:var(--white);text-align:center;padding-top:5px}
.cover__badge-name{font-size:10.5px;font-weight:500;display:block}
.cover__badge-role{font-size:6.2px;display:block;margin-top:1px}

/* back */
.brand--back{left:14px;top:28px;width:210px}
.brand--back .brand__dot{width:26px;height:26px;border-width:3px}
.brand--back .brand__name{font-size:12px}
.copy{font-size:6.5px;line-height:9.6px;color:#444;text-align:justify}
.copy p+p{margin-top:9px}
.copy--intro{left:12px;top:80px;width:184px}
.copy--options{left:231px;top:19px;width:187px}
.copy--fusion{left:231px;top:296px;width:187px}
.copy--replace{left:452px;top:157px;width:173px;font-size:6.1px;line-height:8.7px}
.copy--results{left:452px;top:286px;width:173px;font-size:6.1px;line-height:8.7px}
.section-title{color:var(--teal-strong);font-weight:500;font-size:11.5px;line-height:14px}
.section-title--fusion{left:231px;top:278px}
.section-title--replace{left:452px;top:124px;width:180px}
.section-title--results{left:452px;top:266px}
.xray{border-radius:50%;border:4px solid var(--white);box-shadow:0 1px 5px rgba(0,0,0,.3)}
.xray--heel{left:14px;top:286px;width:146px;height:146px;background:radial-gradient(circle at 45% 45%,#d6d6d6 0%,#8a8a8a 45%,#2c2c2c 100%)}
.xray--fusion{left:256px;top:152px;width:108px;height:108px;background:radial-gradient(circle at 50% 50%,#cfcfcf 0%,#7a7a7a 45%,#1f1f1f 100%)}
.xray--implant{left:472px;top:14px;width:104px;height:104px;background:radial-gradient(circle at 50% 40%,#e2e2e2 0%,#808080 45%,#202020 100%)}
.web-cta{width:210px;text-align:center;color:var(--white)}
.web-cta--mid{left:207px;top:452px}
.web-cta--right{left:424px;top:452px}
.web-cta__lead{font-size:6px;font-weight:300;display:block}
.web-cta__main{font-size:13px;font-weight:500;display:block;line-height:14px;margin-top:2px}
.web-cta__url{font-size:6.4px;display:block}
</style>
</head>
<body>

<div class="side-label side-label--front">FRONT</div>

<section class="sheet sheet--front" aria-label="Brochure outside">
  <div class="panel-tint" style="left:207px;width:210px"></div>
  <div class="abs portrait" role="img" aria-label="Portrait photo of the orthopaedic surgeon in a dark suit"></div>
  <div class="abs hero-photo" role="img" aria-label="Photo of a runner holding a sore ankle in a sunlit field"></div>

  <svg class="decor" viewBox="0 0 634 492" aria-hidden="true">
    <defs>
      <linearGradient id="blueFade" x1="0" y1="0" x2="0" y2="1">
        <stop offset="0" stop-color="#1e78bd"/>
        <stop offset="1" stop-color="#3d8fcb"/>
      </linearGradient>
      <linearGradient id="blueBand" x1="0" y1="0" x2="1" y2="0">
        <stop offset="0" stop-color="#0355a3"/>
        <stop offset="1" stop-color="#0a66b3"/>
      </linearGradient>
    </defs>
    <path d="M0 178 Q100 154 207 184 L207 198 Q100 172 0 194Z" fill="#3fb8a8"/>
    <path d="M0 194 Q100 172 207 198 L207 492 L0 492Z" fill="url(#blueFade)"/>
    <path d="M207 296 C300 302 370 304 417 312 C470 330 560 345 634 350 L634 492 L207 492Z" fill="#f6f7f9"/>
    <path d="M417 312 C470 330 560 345 634 350 L634 492 L417 492Z" fill="#ffffff"/>
    <path d="M417 282 C480 310 570 306 634 288 L634 318 C560 326 480 322 417 300Z" fill="#3fb8a8"/>
    <path d="M417 300 C480 322 560 326 634 318 L634 350 C560 345 470 330 417 312Z" fill="url(#blueBand)"/>
  </svg>

  <div class="abs building-photo" role="img" aria-label="Photo of the private hospital building"></div>

  <h2 class="abs bio bio__name">DR MARTIN ELLERY</h2>
  <p class="abs bio bio__creds">MBBS (EIU), FRACS (Ortho), FA (Ortho)</p>
  <p class="abs bio bio__text">Dr Martin Ellery is an Australian trained Orthopaedic Surgeon who has a primary focus in the treatment of conditions of the foot and ankle. He has completed post fellowship training in Foot and Ankle surgery both locally and internationally, and continues to update himself in the latest techniques.</p>

  <h3 class="abs conditions__title">CONDITIONS TREATED</h3>
  <p class="abs conditions__intro">Dr Ellery provides assessment and treatment of all foot and ankle conditions. He has special interest in the following.</p>
  <ul class="abs conditions__list">
    <li style="top:365px"><svg viewBox="0 0 10 10"><circle cx="5" cy="5" r="4.3" fill="none" stroke="#fff" stroke-width="1"/><path d="M3 5.2l1.4 1.4L7.2 3.6" fill="none" stroke="#fff" stroke-width="1"/></svg>Minimally invasive treatment for bunions and toe deformities.</li>
    <li style="top:381px"><svg viewBox="0 0 10 10"><circle cx="5" cy="5" r="4.3" fill="none" stroke="#fff" stroke-width="1"/><path d="M3 5.2l1.4 1.4L7.2 3.6" fill="none" stroke="#fff" stroke-width="1"/></svg>Joint sparing procedures for arthritis or deformity, including the Flexa implant.</li>
    <li style="top:408px"><svg viewBox="0 0 10 10"><circle cx="5" cy="5" r="4.3" fill="none" stroke="#fff" stroke-width="1"/><path d="M3 5.2l1.4 1.4L7.2 3.6" fill="none" stroke="#fff" stroke-width="1"/></svg>Joint fusion procedures for arthritis of the feet and ankle.</li>
    <li style="top:425px"><svg viewBox="0 0 10 10"><circle cx="5" cy="5" r="4.3" fill="none" stroke="#fff" stroke-width="1"/><path d="M3 5.2l1.4 1.4L7.2 3.6" fill="none" stroke="#fff" stroke-width="1"/></svg>Sports injuries and tendinopathies.</li>
    <li style="top:441px;border-bottom:none"><svg viewBox="0 0 10 10"><circle cx="5" cy="5" r="4.3" fill="none" stroke="#fff" stroke-width="1"/><path d="M3 5.2l1.4 1.4L7.2 3.6" fill="none" stroke="#fff" stroke-width="1"/></svg>Total ankle replacement and deformity correction of the foot and ankle.</li>
  </ul>

  <h3 class="abs contact contact__title">CONTACT US</h3>
  <ul class="abs contact contact__list">
    <li><svg viewBox="0 0 10 10"><path d="M5 0.5a3.3 3.3 0 0 0-3.3 3.3C1.7 6.3 5 9.5 5 9.5s3.3-3.2 3.3-5.7A3.3 3.3 0 0 0 5 0.5zm0 4.6a1.3 1.3 0 1 1 0-2.6 1.3 1.3 0 0 1 0 2.6z" fill="#0355a3"/></svg>Suite 410, Level 4</li>
    <li>Harbourside Private Hospital</li>
    <li>220 Marine Parade Eastport NSW</li>
    <li><svg viewBox="0 0 10 10"><path d="M5 0.5a3.3 3.3 0 0 0-3.3 3.3C1.7 6.3 5 9.5 5 9.5s3.3-3.2 3.3-5.7A3.3 3.3 0 0 0 5 0.5zm0 4.6a1.3 1.3 0 1 1 0-2.6 1.3 1.3 0 0 1 0 2.6z" fill="#0355a3"/></svg>15 Ridge Road Kellow NSW</li>
    <li><svg viewBox="0 0 10 10"><path d="M2.2 0.8l1.6 0 .8 2.2-1.1.8a5.5 5.5 0 0 0 2.6 2.6l.8-1.1 2.2.8v1.6c0 .6-.5 1-1.1 1A7.9 7.9 0 0 1 1.2 1.9c0-.6.4-1.1 1-1.1z" fill="#0355a3"/></svg>(02) 5550 1234</li>
    <li><svg viewBox="0 0 10 10"><rect x="2.5" y="1" width="5" height="2.5" fill="#0355a3"/><rect x="1" y="3.5" width="8" height="4" rx=".6" fill="#0355a3"/><rect x="2.8" y="6" width="4.4" height="3" fill="#fff" stroke="#0355a3" stroke-width=".8"/></svg>(02) 5550 1299</li>
    <li><svg viewBox="0 0 10 10"><rect x=".8" y="2" width="8.4" height="6" fill="#0355a3"/><path d="M.8 2L5 5.5 9.2 2" fill="none" stroke="#fff" stroke-width=".8"/></svg>info@hollowbrookclinic.com.au</li>
    <li><svg viewBox="0 0 10 10"><circle cx="5" cy="5" r="4" fill="none" stroke="#0355a3" stroke-width="1"/><ellipse cx="5" cy="5" rx="1.8" ry="4" fill="none" stroke="#0355a3" stroke-width=".8"/><path d="M1 5h8" stroke="#0355a3" stroke-width=".8"/></svg>www.hollowbrookclinic.com.au</li>
  </ul>
  <div class="abs brand brand--contact"><span class="brand__dot"></span><span class="brand__name">Hollowbrook Clinic</span></div>

  <h1 class="abs cover__title">MY PAINFUL ANKLE</h1>
  <p class="abs cover__sub">SOLUTIONS FOR ANKLE ARTHRITIS</p>
  <div class="abs cover__badge">
    <span class="cover__badge-name">DR MARTIN ELLERY</span>
    <span class="cover__badge-role">ORTHOPAEDIC FOOT AND ANKLE SURGEON</span>
  </div>
  <div class="abs brand brand--cover"><span class="brand__dot"></span><span class="brand__name">Hollowbrook Clinic</span></div>
</section>

<section class="sheet sheet--back" aria-label="Brochure inside">
  <div class="panel-tint" style="left:417px;width:217px"></div>
  <svg class="decor" viewBox="0 0 634 492" aria-hidden="true">
    <defs>
      <linearGradient id="footBand" x1="0" y1="0" x2="1" y2="0">
        <stop offset="0" stop-color="#0355a3"/>
        <stop offset=".55" stop-color="#0a6cb8"/>
        <stop offset="1" stop-color="#0355a3"/>
      </linearGradient>
    </defs>
    <path d="M0 268 C50 290 120 350 207 400 L207 492 L0 492Z" fill="#1a6fb8"/>
    <path d="M0 258 C40 270 70 290 100 310 L92 318 C60 296 30 280 0 272Z" fill="#33a6d7"/>
    <path d="M0 420 C180 470 400 440 634 404" fill="none" stroke="#85cae6" stroke-width="2"/>
    <path d="M0 428 C180 476 400 448 634 410 L634 492 L0 492Z" fill="url(#footBand)"/>
  </svg>

  <div class="abs brand brand--back"><span class="brand__dot"></span><span class="brand__name">Hollowbrook Clinic</span></div>
  <div class="abs copy copy--intro">
    <p>Ankle arthritis is a painful condition where there is loss of cartilage from the ankle joint surface. Although not as common as knee or hip arthritis, pain can be debilitating affecting quality of life.</p>
    <p>Arthritis of the joint can be caused by trauma joint such as fracture or recurrent instability or secondary from inflammatory conditions such as rheumatoid arthritis.</p>
    <p>Pain from the joint will occur with activity causing a limp, limiting walking speed and distance. Often there is swelling of the joint with progressive loss of motion.</p>
    <p>Diagnosis is made with examination of the ankle and weight bearing x-rays showing loss of joint space.</p>
  </div>
  <div class="abs xray xray--heel" role="img" aria-label="X-ray of an arthritic ankle"></div>

  <div class="abs copy copy--options">
    <p>When pain medication, activity modification and shoe ware modification is no longer effective to control the pain then it is worthwhile discussing with your GP for referral to Dr Martin Ellery for an opinion on further treatment. As an Orthopaedic Foot and Ankle surgeon, he will be able to assess your conditions and give advice on the best options for your treatment.</p>
    <p>The decision on the best option is based on your age, activity level, existing medical problems, previous ankle treatment and your expected outcome from treatment. In the situation of end stage arthritis options consist of either Ankle fusion or Total Ankle replacement.</p>
  </div>
  <div class="abs xray xray--fusion" role="img" aria-label="X-ray of an ankle fused with plates and screws"></div>
  <h3 class="abs section-title section-title--fusion">ANKLE FUSION SURGERY</h3>
  <div class="abs copy copy--fusion">
    <p>This operation aims to stiffen the ankle joint by fusing the tibia and talus together in the optimal position for function. The common thought is that there will be no movement of the foot, and the patient will walk with a limp. The fusion only occurs at the ankle joint, leaving motion available to the surrounding joints. Although there is decreased motion, you will walk more normally after a fusion without a limp as the pain to the joint is removed.</p>
  </div>

  <div class="abs xray xray--implant" role="img" aria-label="X-ray of a total ankle replacement implant"></div>
  <h3 class="abs section-title section-title--replace">TOTAL ANKLE REPLACEMENT SURGERY</h3>
  <div class="abs copy copy--replace">
    <p>In suitable patients there may be the option to maintain joint motion and perform a Total Ankle Replacement. Like a hip or knee replacement operation, the arthritic joint is removed and replaced with an artificial joint. Like an ankle fusion there will alleviation of the pain and limp with maintenance of the ankle joint motion. Recovery to walking post-surgery is often much sooner than with ankle fusion. Dr Martin Ellery is one of the few surgeons to have completed an international fellowship in ankle replacement surgery and has been performing the technique since 2008. He is currently performing the technique using the Meridian total ankle with patient-specific guides.</p>
  </div>
  <h3 class="abs section-title section-title--results">RESULTS OF SURGERY</h3>
  <div class="abs copy copy--results">
    <p>Successful surgery in the suitable patient will help resolve the pain associated with the ankle arthritis. Ankle Fusion surgery is ideal for patients with heavy labour work, allowing them to return to previous activities. There may be the risk of arthritis to surrounding joints in the future, but often this occurs many years down the track. Results from Total Ankle replacement surgery have been improving over the years, but there is known risks of loosening, cyst formation or failure of the joint over time that can occur in some patients. It is important to have a opinion from an Orthopaedic Foot and Ankle Surgeon experienced in the these procedure to determine which procedure will provide the best long term solution for you.</p>
  </div>

  <div class="abs web-cta web-cta--mid">
    <span class="web-cta__lead">For more information on ankle fusion, risks and recovery</span>
    <span class="web-cta__main">visit our website</span>
    <span class="web-cta__url">www.hollowbrookclinic.com.au/Ankle-Replacement</span>
  </div>
  <div class="abs web-cta web-cta--right">
    <span class="web-cta__lead">For more information on ankle fusion, risks and recovery</span>
    <span class="web-cta__main">visit our website</span>
    <span class="web-cta__url">www.hollowbrookclinic.com.au/Ankle-Replacement</span>
  </div>
</section>

<div class="side-label side-label--back">BACK</div>

</body>
</html>
```